Our companies name is The Gilded Ladle and we specialize in craft cupcakes, what I mean by that is that we bake our cupcakes with craft beer and other alcoholic drinks. We are trying to focus on being elegant but at the same time unpretentious. Since we are incorporating beer in our cupcakes we want the business card to have our logo in the front and our information in the back.

Once we select the best design we will provide the contact information to be added. Thank you.

Industry/Entity Type

Business

Font styles to use
Decorative
Script

Requirements
Must have
• Round corners
Should not have
• Square corners

```html
<!DOCTYPE html>
<html lang="en">
<head>
<meta charset="utf-8">
<title>The Gilded Ladle – Business Card</title>
<link rel="stylesheet" href="https://fonts.googleapis.com/css2?family=Poiret+One&family=Libre+Baskerville&family=Dancing+Script&display=swap">
<style>
  :root {
    --backdrop: #2a2a2a;
    --card-black: #0c0c0c;
    --card-red: #e8232f;
    --rule-red: #b3202a;
    --rule-dark: #1a1a1a;
    --teal: #7fd1c3;
  }
  html, body {
    margin: 0;
    width: 1200px;
    height: 900px;
    overflow: hidden;
    background: var(--backdrop);
  }
  .canvas {
    position: relative;
    width: 1200px;
    height: 900px;
  }
  .card {
    position: absolute;
    left: 320px;
    width: 560px;
    height: 320px;
    border-radius: 22px;
    overflow: hidden;
    background: var(--card-black);
  }
  .card--front { top: 70px; }
  .card--back { top: 480px; }
  .card-art {
    position: absolute;
    inset: 0;
    width: 100%;
    height: 100%;
  }
  .brand-name {
    position: absolute;
    left: 0;
    right: 0;
    text-align: center;
    margin: 0;
    font-family: "Libre Baskerville", serif;
    font-weight: 400;
    color: var(--teal);
    letter-spacing: 2px;
  }
  .card--front .brand-name {
    top: 142px;
    font-size: 30px;
  }
  .card--back .brand-name {
    top: 62px;
    font-size: 22px;
  }
  .contact {
    position: absolute;
    left: 0;
    right: 0;
    top: 172px;
    text-align: center;
    color: var(--teal);
  }
  .contact-name {
    margin: 0;
    font-family: "Poiret One", sans-serif;
    font-size: 36px;
    letter-spacing: 6px;
    line-height: 1;
  }
  .contact-value {
    margin: 10px 0 0;
    font-family: "Libre Baskerville", serif;
    font-size: 18px;
    line-height: 1.1;
  }
  .contact-value + .contact-value { margin-top: 6px; }
  .contact-label {
    display: block;
    font-family: "Dancing Script", cursive;
    font-size: 13px;
    line-height: 1;
  }
</style>
</head>
<body>
<main class="canvas">

  <section class="card card--front" aria-label="Card front">
    <svg class="card-art" viewBox="0 0 560 320" aria-hidden="true">
      <rect x="12" y="12" width="536" height="296" rx="14" fill="none" stroke="var(--rule-red)" stroke-width="1.5"/>
    </svg>
    <h1 class="brand-name">The Gilded Ladle</h1>
  </section>

  <section class="card card--back" aria-label="Card back">
    <svg class="card-art" viewBox="0 0 560 320" aria-hidden="true">
      <path class="red-band" d="M0 124 Q280 176 560 124 L560 320 L0 320 Z" fill="var(--card-red)"/>
      <rect x="12" y="12" width="536" height="296" rx="14" fill="none" stroke="var(--rule-red)" stroke-width="1.2"/>
      <path class="band-rule" d="M12 130 Q280 180 548 130" fill="none" stroke="var(--rule-dark)" stroke-width="1.2"/>
    </svg>
    <h2 class="brand-name">The Gilded Ladle</h2>
    <div class="contact">
      <p class="contact-name">ROSA DELGADO</p>
      <p class="contact-value">(555) 014-2837<span class="contact-label">phone</span></p>
      <p class="contact-value">thegildedladle@postmail.com<span class="contact-label">email</span></p>
    </div>
  </section>

</main>
</body>
</html>
```